Letterhead and compliment slip

We are a UK-based market research agency. We are looking for a new letterhead design to incorporate our logo, address details and company information. We are looking for a simple design. It should be modern. It needs to have a qualify feel. As we are UK based it needs to be designed for A4 paper size (letterhead).
I'm really looking for something simple in design terms!
Both letterhead and compliment slip need to include:
Our logo
Company address
Telephone number
Email address
Website address
Company registration number
VAT registration number
Grey and green would be a good colour scheme to fit with our logo

```html
<!DOCTYPE html>
<html lang="en">
<head>
<meta charset="utf-8">
<title>Northlight Consumer Research – Letterhead and Compliment Slip</title>
<link href="https://fonts.googleapis.com/css2?family=Fira+Sans:wght@400;500;600&display=swap" rel="stylesheet">
<style>
  :root {
    --backdrop: #ebebeb;
    --paper: #ffffff;
    --brand-green: #a3c93a;
    --brand-green-light: #cfdf3f;
    --ink: #2b2b2b;
    --muted: #8a8a8a;
  }
  * { margin: 0; padding: 0; box-sizing: border-box; }
  html, body { width: 1200px; height: 1200px; overflow: hidden; }
  body {
    background: var(--backdrop);
    font-family: "Fira Sans", Arial, sans-serif;
    color: var(--ink);
    position: relative;
  }
  .sheet {
    position: absolute;
    background: var(--paper);
    box-shadow: 0 18px 40px rgba(0,0,0,0.12);
  }

  /* Letterhead (A4) */
  .letterhead { left: 56px; top: 94px; width: 718px; height: 1015px; }
  .wordmark {
    display: flex; align-items: center; gap: 7px;
    color: var(--brand-green); font-weight: 600; font-size: 30px; letter-spacing: -0.3px;
  }
  .wordmark__dot { width: 20px; height: 20px; border-radius: 50%; background: var(--brand-green); }
  .letterhead .wordmark { position: absolute; top: 24px; left: 0; right: 0; justify-content: center; }
  .letterhead__address {
    position: absolute; top: 83px; left: 0; right: 0;
    text-align: center; font-size: 10.5px; line-height: 18.5px;
  }
  .letterhead__rule {
    position: absolute; top: 128px; left: 0; right: 0; height: 3px;
  }
  .letterhead__rule::before, .letterhead__rule::after {
    content: ""; position: absolute; top: 0; height: 3px; background: var(--brand-green);
  }
  .letterhead__rule::before { left: 0; width: 253px; }
  .letterhead__rule::after { right: 0; width: 254px; }
  .letterhead__web {
    position: absolute; top: 120px; left: 0; right: 0; text-align: center;
    font-size: 10.5px; letter-spacing: 1.6px;
  }
  .letterhead__registration {
    position: absolute; left: 66px; top: 901px; height: 73px;
    border-left: 3px solid var(--brand-green);
    padding-left: 25px; padding-top: 19px;
    font-size: 10.5px; line-height: 21.5px;
  }

  /* Compliment slip */
  .slip { left: 812px; top: 392px; width: 338px; height: 718px; overflow: hidden; }
  .slip__frame {
    position: absolute; left: 0; top: 0; width: 718px; height: 338px;
    transform-origin: 0 0; transform: translateX(338px) rotate(90deg);
  }
  .slip__pattern {
    position: absolute; left: 0; top: 0; width: 268px; height: 170px;
    background: linear-gradient(135deg, var(--brand-green-light) 0%, var(--brand-green) 55%, rgba(163,201,58,0.15) 100%);
    clip-path: polygon(0 0, 100% 0, 72% 100%, 40% 70%, 18% 100%, 0 60%);
  }
  .slip .wordmark { position: absolute; left: 72px; top: 194px; font-size: 28px; }
  .wordmark--vertical .wordmark__dot { width: 18px; height: 18px; }
  .slip__address {
    position: absolute; left: 32px; top: 258px; font-size: 10.5px; line-height: 19px;
  }
  .slip__contact {
    position: absolute; left: 32px; top: 302px; font-size: 10.5px;
  }
  .slip__divider {
    position: absolute; left: 316px; top: 309px; width: 146px; height: 2px; background: var(--brand-green);
  }
  .slip__web {
    position: absolute; left: 476px; top: 302px; font-size: 11px; letter-spacing: 1.7px;
  }
  .slip__edge {
    position: absolute; left: 252px; top: 17px; width: 444px; height: 2px; background: var(--brand-green);
  }
</style>
</head>
<body>

<section class="sheet letterhead" aria-label="A4 letterhead">
  <div class="wordmark"><span class="wordmark__dot"></span>Northlight</div>
  <p class="letterhead__address">
    Northlight Consumer Research Ltd. | &nbsp;12 Willow Yard | Mill Lane | Beechfield | Harpenden | &nbsp;Hertfordshire | AL5 2QT<br>
    +44 (0)1632 960418 | &nbsp;info@northlightresearch.co.uk
  </p>
  <div class="letterhead__rule"></div>
  <p class="letterhead__web">www.northlightresearch.co.uk</p>
  <div class="letterhead__registration">
    VAT Registration Number : 746203158<br>
    Company Registration Number : 4816270
  </div>
</section>

<section class="sheet slip" aria-label="Compliment slip">
  <div class="slip__frame">
    <div class="slip__pattern" role="img" aria-label="Decorative cluster of green triangles"></div>
    <div class="wordmark wordmark--vertical"><span class="wordmark__dot"></span>Northlight</div>
    <p class="slip__address">
      Northlight Consumer Research Ltd. | 12 Willow Yard | Mill Lane<br>
      Beechfield | Harpenden | Hertfordshire | AL5 2QT
    </p>
    <p class="slip__contact">info@northlightresearch.co.uk | +44 (0)1632 960418</p>
    <div class="slip__divider"></div>
    <p class="slip__web">www.northlightresearch.co.uk</p>
    <div class="slip__edge"></div>
  </div>
</section>

</body>
</html>
```